7K Ventures business cards for a tech VC

We're starting a new Venture Capital that is focusing on bringing the best start ups from Israel to NYC
We need a business cards template for this that gives the sense of an entrepreneurial look
I don't want any religious signs on this even thought it's Israel
I'm looking for a techi feeling but not too crazy
The card should probably be in the same light blue as the logo and the logo in white

Target Market(s)

Investors

Industry/Entity Type

Tech

Contact Information for Business Card

The card needs to look slick and entrepreneurship like
The VC is focused on NYC and Tel Aviv so could be great to show something on the back side that is like NYC skyline or something like that
You can see the logo attached

Colors
0455a3
3276b5
85acd3
cedeed
eaf1f7

Requirements
Must have
• A very cool looking business card that shows we're a cutting edge tech VC with a focus on bringing start ups from Tel Aviv and leveraging the NYC ecosystem
Nice to have
• NYC skyline can be cool , maybe something that is connected to Tel Aviv

```html
<!DOCTYPE html>
<html lang="en">
<head>
<meta charset="utf-8">
<title>7K Ventures – Business Cards</title>
<link href="https://fonts.googleapis.com/css2?family=Lato:wght@400;700&display=swap" rel="stylesheet">
<style>
  :root {
    --canvas: #3a3b3d;
    --card-blue: #2f74b7;
    --accent-blue: #1b8fd2;
    --white: #ffffff;
    --shadow: rgba(0, 0, 0, 0.35);
  }
  * { margin: 0; padding: 0; box-sizing: border-box; }
  html, body {
    width: 1200px; height: 900px; overflow: hidden;
    background: var(--canvas);
    font-family: "Lato", sans-serif;
  }
  .stage { position: relative; width: 1200px; height: 900px; }
  .card {
    position: absolute; left: 280px; width: 640px; height: 366px;
    box-shadow: 0 10px 24px var(--shadow); overflow: hidden;
  }
  .card-back { top: 50px; background: var(--card-blue); }
  .card-front { top: 470px; background: var(--white); }

  .brand-name { font-weight: 700; letter-spacing: 1px; line-height: 1; }

  .card-back .brand {
    position: absolute; left: 0; right: 0; top: 120px; text-align: center;
  }
  .card-back .brand-name { color: var(--white); font-size: 58px; }
  .card-back .web {
    position: absolute; left: 0; right: 0; top: 236px; text-align: center;
    color: var(--white); font-size: 17px; letter-spacing: 1px;
  }

  .front-bg { position: absolute; inset: 0; width: 100%; height: 100%; }
  .card-front .brand { position: absolute; left: 40px; top: 44px; }
  .card-front .brand-name { color: var(--card-blue); font-size: 52px; }

  .address {
    position: absolute; left: 34px; top: 252px;
    color: var(--white); font-size: 17px; line-height: 1.3;
  }
  .contact {
    position: absolute; right: 34px; top: 206px; text-align: right;
    color: var(--white);
  }
  .person-name { font-size: 24px; font-weight: 700; }
  .person-role { font-size: 16px; margin-bottom: 10px; }
  .contact-line {
    display: flex; justify-content: flex-end; align-items: center; gap: 10px;
    font-size: 16px; line-height: 1.35;
  }
  .contact-line svg { width: 15px; height: 15px; fill: var(--white); flex: none; }
</style>
</head>
<body>
<main class="stage">

  <section class="card card-back">
    <div class="brand"><span class="brand-name">7K VENTURES</span></div>
    <p class="web">www.7kventures.com</p>
  </section>

  <section class="card card-front">
    <svg class="front-bg" viewBox="0 0 640 366" preserveAspectRatio="none" aria-hidden="true">
      <path d="M0 190 C170 280 430 300 640 70 L640 366 L0 366 Z" fill="var(--card-blue)"/>
      <path d="M240 282 C420 290 560 230 625 74 C555 215 420 278 240 282 Z" fill="var(--accent-blue)"/>
    </svg>

    <div class="brand"><span class="brand-name">7K VENTURES</span></div>

    <p class="address">4100 Lane Road<br>Marlow TX 78010</p>

    <div class="contact">
      <p class="person-name">Daniel Orsen</p>
      <p class="person-role">Manager</p>
      <p class="contact-line">555 014 2200
        <svg viewBox="0 0 16 16"><path d="M3 1l3 3-1.6 2a9 9 0 0 0 5.6 5.6L12 10l3 3-2 2C7 15 1 9 1 3z"/></svg>
      </p>
      <p class="contact-line">555 014 2201
        <svg viewBox="0 0 16 16"><path d="M4 1h8v4H4zM1 6h14v6h-3v3H4v-3H1zM5 10v4h6v-4z"/></svg>
      </p>
      <p class="contact-line">info@7kventures.com
        <svg viewBox="0 0 16 16"><path d="M1 3h14v10H1zM2 4l6 5 6-5v-.1H2z" fill-rule="evenodd"/></svg>
      </p>
      <p class="contact-line">www.7kventures.com
        <svg viewBox="0 0 16 16"><path d="M8 1a7 7 0 1 0 0 14A7 7 0 0 0 8 1zm0 1.5c.9 0 1.9 2 2.1 4.7H5.9C6.1 4.5 7.1 2.5 8 2.5zM2.6 8.8h2.3c.1 1.8.5 3.3 1 4.3a5.5 5.5 0 0 1-3.3-4.3zm0-1.6a5.5 5.5 0 0 1 3.3-4.3c-.5 1-.9 2.5-1 4.3zm3.3 1.6h4.2c-.2 2.7-1.2 4.7-2.1 4.7s-1.9-2-2.1-4.7zm4.2-5.9a5.5 5.5 0 0 1 3.3 4.3h-2.3c-.1-1.8-.5-3.3-1-4.3zm1 5.9h2.3a5.5 5.5 0 0 1-3.3 4.3c.5-1 .9-2.5 1-4.3z"/></svg>
      </p>
    </div>
  </section>

</main>
</body>
</html>
```